Project: PLWT Biz Cards
PLWT Biz Cards - Construction
Professional
Derek M. Hollis
not using an address on biz cards
derek.hollis@pave-ro.com
www.patiotilesmadebest.com
We are interested in biz card and all stationary items!! Our logo is attached. If you chose not to use our logo, definitely incorporate the logo's look and feel. Use icons to stipulate phone, fax, website, etc rather than words.
Use logo or other design.
Garage Garage
we are running out of time. 6 minutes Did you get my other emails? Just fretting a bit. :-)

```html
<!DOCTYPE html>
<html lang="en">
<head>
<meta charset="utf-8">
<title>PLWT Business Card</title>
<link rel="stylesheet" href="https://fonts.googleapis.com/css2?family=Raleway:wght@300;400;600;800&display=swap">
<style>
  :root {
    --backdrop: #e6e4e0;
    --card-black: #0d0d0d;
    --ink: #1c1c1c;
    --ink-soft: #4a4a4a;
    --paper-text: #ffffff;
    --accent: #c8161d;
  }
  * { margin: 0; padding: 0; box-sizing: border-box; }
  html, body {
    width: 1200px; height: 1086px; overflow: hidden;
    background: var(--backdrop);
    font-family: "Raleway", sans-serif;
  }
  .business-card {
    position: absolute; left: 100px; top: 258px;
    width: 1000px; height: 570px;
    background: linear-gradient(90deg, #dcdcdc 0%, #ffffff 60%, #f1f1f1 100%);
    box-shadow: 0 18px 40px rgba(0,0,0,.28);
    overflow: hidden;
  }
  .dark-panel { position: absolute; inset: 0; }
  .contact {
    position: absolute; right: 540px;
    color: var(--paper-text);
    font-size: 22px; font-weight: 400; line-height: 1.5; letter-spacing: .5px;
    text-align: right; white-space: nowrap;
  }
  .contact--phone { top: 117px; }
  .contact--email { top: 268px; }
  .contact--web { top: 403px; }
  .brand {
    position: absolute; left: 640px; top: 175px;
    display: flex; align-items: center; gap: 16px;
    color: var(--ink);
  }
  .brand__dot { width: 34px; height: 34px; border-radius: 50%; background: var(--accent); }
  .brand__name { font-size: 64px; font-weight: 800; letter-spacing: 3px; line-height: 1; }
  .identity { position: absolute; left: 640px; top: 300px; color: var(--ink); }
  .identity__name {
    font-size: 30px; font-weight: 400; letter-spacing: 3px; text-transform: uppercase;
  }
  .identity__title { font-size: 22px; font-weight: 300; color: var(--ink-soft); margin-top: 6px; }
</style>
</head>
<body>
  <div class="business-card">
    <svg class="dark-panel" width="1000" height="570" viewBox="0 0 1000 570" aria-hidden="true">
      <g fill="var(--card-black)">
        <rect x="0" y="0" width="520" height="570"/>
        <circle cx="520" cy="150" r="48"/>
        <circle cx="520" cy="285" r="48"/>
        <circle cx="520" cy="420" r="48"/>
      </g>
      <g fill="none" stroke="#fff" stroke-width="2.5">
        <circle cx="524" cy="150" r="26"/>
        <circle cx="524" cy="285" r="26"/>
        <circle cx="524" cy="420" r="26"/>
      </g>
      <path fill="#fff" d="M515 138 c3-2 5 0 6 3 l2 5 c1 2 0 3-2 4 c1 4 4 7 8 9 c1-2 2-3 4-2 l5 2 c3 1 5 3 3 6 c-2 4-6 5-10 3 c-9-4-15-10-18-19 c-1-4 0-8 2-11z"/>
      <g fill="none" stroke="#fff" stroke-width="2">
        <rect x="511" y="276" width="26" height="18" rx="2"/>
        <path d="M511 277 L524 287 L537 277"/>
      </g>
      <g fill="none" stroke="#fff" stroke-width="2">
        <circle cx="524" cy="420" r="13"/>
        <ellipse cx="524" cy="420" rx="6" ry="13"/>
        <line x1="511" y1="420" x2="537" y2="420"/>
        <line x1="513" y1="413" x2="535" y2="413"/>
        <line x1="513" y1="427" x2="535" y2="427"/>
      </g>
    </svg>

    <p class="contact contact--phone">014 728 3051<br>014 728 3052</p>
    <p class="contact contact--email">derek.hollis@pave-ro.com</p>
    <p class="contact contact--web">www.patiotilesmadebest.com</p>

    <div class="brand">
      <span class="brand__dot"></span>
      <span class="brand__name">PLWT</span>
    </div>

    <div class="identity">
      <h1 class="identity__name">Derek M. Hollis</h1>
      <p class="identity__title">Managing Director</p>
    </div>
  </div>
</body>
</html>
```